NEW FACEBOOK AD CREATIVES FOR MARKETING AGENCY

We need one single static image AND a Carousel Ad Design With 5 Cards Total in it.

We advertise a SaaS Product that teaches businesses how to use incentive based marketing to get more sales and leads.

Using our service businesses can give away smart devices like smartwatches, earpods, mp4 players, tablets, etc. as a gift bonus along with their product or service as an added value benefit to help them create more attractive offers and to get more sales.

I have attached two designs that get me my best results on facebook ads so far so I want to create something very similar with a different look and showcasing 3-4 of the items I have attached images for.

CONTENT & INSTRUCTIONS:
MAIN TEXT: TRIPLE YOUR SALES OFFERING FREE SMART DEVICES AS A BONUS FOR BUYING YOUR PRODUCT OR SERVICE

Target Market(s)

ENTREPRENEURS, INVESTORS, BUSINESS OWNERS, MEDIA AGENCIES, BROKERAGES

Industry/Entity Type

marketing gifting

Requirements
Must have
• must match color scheme of website www.brightlanepromoworks.biz as this is where they will be redirected to when they click.
Nice to have
• the ads must be 1080x1080 Static newsfeed ad and carousel ads

```html
<!DOCTYPE html>
<html lang="en">
<head>
<meta charset="utf-8">
<title>Brightlane Promoworks – Static and Carousel Ads</title>
<link href="https://fonts.googleapis.com/css2?family=Barlow+Condensed:ital,wght@0,700;0,800;1,700;1,800&family=Poppins:wght@600;700&family=Montserrat:wght@500;600;700&display=swap" rel="stylesheet">
<style>
  :root {
    --page: #f1f0ee;
    --royal: #1a55f2;
    --royal-deep: #0f3fd8;
    --navy: #1d1d8c;
    --green: #3fe12b;
    --red: #ff3a1c;
    --cta: #f0321c;
    --yellow: #f0d21a;
    --yellow-deep: #e7a818;
    --orange: #f04a1c;
    --purple: #8b2f9e;
    --white: #ffffff;
    --ink: #1b1b1b;
  }
  * { box-sizing: border-box; margin: 0; padding: 0; }
  html, body { width: 1200px; height: 1029px; overflow: hidden; background: var(--page); }
  body { position: relative; font-family: "Montserrat", sans-serif; }

  .brand { display: flex; align-items: center; gap: 6px; color: var(--royal-deep);
    font-family: "Barlow Condensed", sans-serif; font-weight: 800; letter-spacing: .5px; white-space: nowrap; }
  .brand .dot { width: 10px; height: 10px; border-radius: 50%; background: var(--royal-deep); }

  /* ---------- static ad ---------- */
  .static-ad { position: absolute; left: 290px; top: 24px; width: 620px; height: 620px;
    background: linear-gradient(160deg, var(--royal) 0%, #1e5cf5 60%, var(--royal-deep) 100%); overflow: hidden; }
  .static-ad .corner { position: absolute; inset: 0; }
  .static-ad .brand { position: absolute; left: 30px; top: 22px; font-size: 18px; }
  .headline { position: absolute; left: 0; right: 0; text-align: center; color: var(--white);
    font-family: "Barlow Condensed", sans-serif; font-weight: 800; line-height: 1; }
  .static-ad .h-top { top: 92px; font-size: 38px; }
  .static-ad .h-big { top: 128px; font-size: 66px; letter-spacing: .5px; }
  .h-big .go { color: var(--green); }
  .h-big .free { color: var(--red); }
  .sub { font-style: italic; font-weight: 700; }
  .sub .bonus { color: var(--red); }
  .static-ad .sub { top: 198px; font-size: 25px; line-height: 1.15; }

  .device { position: absolute; border-radius: 50%; border: 2px solid rgba(255,255,255,.45); }
  .static-ad .device { top: 287px; width: 128px; height: 128px; }
  .fill-watch { background: radial-gradient(circle at 45% 40%, #4a4f5c 0%, #16181d 55%, #3b7fe8 100%); }
  .fill-buds { background: radial-gradient(circle at 50% 45%, #ffffff 0%, #e2e4e8 45%, #3b7fe8 100%); }
  .fill-phones { background: radial-gradient(circle at 50% 45%, #7a2a1e 0%, #1a1a1a 45%, #3b7fe8 100%); }
  .fill-speaker { background: radial-gradient(ellipse at 50% 50%, #34373d 0%, #1b1c20 42%, #3b7fe8 100%); }

  .static-ad .chart { position: absolute; left: 0; top: 430px; }
  .static-ad .note { position: absolute; left: 0; right: 0; top: 482px; text-align: center;
    color: var(--white); font-size: 11px; font-weight: 600; line-height: 1.25; }

  .perks { position: absolute; left: 62px; right: 50px; top: 514px; display: flex; justify-content: space-between; }
  .perk { width: 70px; display: flex; flex-direction: column; align-items: center; gap: 5px; color: var(--white); }
  .perk svg { width: 34px; height: 34px; }
  .perk span { font-size: 5.5px; font-weight: 600; text-align: center; line-height: 1.2; }

  .cta { display: inline-block; background: var(--cta); color: var(--white); font-weight: 700;
    border-radius: 20px; white-space: nowrap; }
  .static-ad .cta { position: absolute; left: 213px; top: 577px; width: 196px; height: 32px;
    line-height: 32px; text-align: center; font-size: 12px; }

  /* ---------- carousel ---------- */
  .carousel { position: absolute; left: 12px; top: 680px; display: flex; gap: 14px; }
  .card { position: relative; width: 224px; height: 224px; overflow: hidden; }
  .card .title { position: absolute; left: 0; right: 0; top: 14px; text-align: center; color: var(--white);
    font-family: "Poppins", sans-serif; font-weight: 700; font-size: 18px; white-space: nowrap; }
  .card .photo { position: absolute; }
  .card .cta { position: absolute; left: 50%; transform: translateX(-50%); font-size: 9px; padding: 4px 10px; border-radius: 3px; }
  .card .url { position: absolute; left: 0; right: 0; bottom: 8px; text-align: center; font-size: 7px; color: rgba(0,0,0,.55); }

  .card-intro { background: linear-gradient(150deg, #2a2a9c 0%, var(--navy) 55%, #2b3fb8 100%); }
  .card-intro .brand { position: absolute; left: 12px; top: 10px; font-size: 11px; gap: 4px; }
  .card-intro .brand .dot { width: 7px; height: 7px; }
  .card-intro .h-top { top: 86px; font-size: 18px; }
  .card-intro .h-big { top: 104px; font-size: 31px; }
  .card-intro .sub { top: 140px; font-size: 12px; line-height: 1.15; }
  .card-intro .cta { bottom: 6px; font-size: 7px; padding: 3px 8px; border-radius: 10px; }

  .card-watch { background: linear-gradient(135deg, #1d59f0 0%, var(--royal) 50%, #2e86f2 100%); }
  .card-watch .contact { position: absolute; right: 56px; bottom: 12px; color: var(--ink); text-align: right; }
  .card-watch .contact small { display: block; font-size: 6px; font-weight: 500; }
  .card-watch .contact strong { font-size: 12px; font-weight: 700; }
  .card-watch .call { position: absolute; right: 36px; bottom: 14px; width: 16px; height: 20px; }

  .card-buds { background: linear-gradient(135deg, var(--yellow-deep) 0%, var(--yellow) 55%, #f5d93a 100%); }
  .card-phones { background: linear-gradient(135deg, #e8321a 0%, var(--orange) 55%, #f27222 100%); }
  .card-phones .cta { background: #2e8bf5; }
  .card-bundle { background: linear-gradient(135deg, #b04ab8 0%, var(--purple) 55%, #6e2386 100%); }
</style>
</head>
<body>

<section class="static-ad" aria-label="Static newsfeed ad">
  <svg class="corner" width="620" height="620" aria-hidden="true">
    <polygon points="0,0 456,0 0,89" fill="#ffffff"/>
  </svg>
  <div class="brand"><span class="dot"></span>BRIGHTLANE PROMOWORKS</div>

  <p class="headline h-top">TRIPLE YOUR SALES</p>
  <p class="headline h-big"><span class="go">OFFERING</span> <span class="free">FREE</span></p>
  <p class="headline sub">SMART DEVICES AS A <span class="bonus">BONUS</span> FOR<br>BUYING YOUR PRODUCT OR SERVICE</p>

  <div class="device fill-watch" style="left:30px" role="img" aria-label="Photo of a black smartwatch"></div>
  <div class="device fill-buds" style="left:170px" role="img" aria-label="Photo of white wireless earbuds in their case"></div>
  <div class="device fill-phones" style="left:313px" role="img" aria-label="Photo of black and gold over-ear headphones"></div>
  <div class="device fill-speaker" style="left:454px" role="img" aria-label="Photo of a black portable bluetooth speaker"></div>

  <svg class="chart" width="620" height="90" aria-hidden="true">
    <polyline points="0,76 54,65 133,75 209,45 372,25 455,55 620,12" fill="none" stroke="#f3d51e" stroke-width="2.5"/>
    <g fill="#ffffff" stroke="#f3d51e" stroke-width="1.5">
      <circle cx="54" cy="65" r="5"/><circle cx="133" cy="75" r="5"/><circle cx="209" cy="45" r="5"/>
      <circle cx="372" cy="25" r="5"/><circle cx="455" cy="55" r="5"/>
    </g>
  </svg>
  <p class="note">WITHOUT HAVING TO PERSONALLY<br>FULFILL OR PAY FOR ANY OF THEM YOURSELF!</p>

  <div class="perks">
    <div class="perk">
      <svg viewBox="0 0 34 34" aria-hidden="true"><circle cx="17" cy="17" r="15.5" fill="none" stroke="#fff" stroke-width="1.2"/><rect x="9" y="12" width="16" height="10" rx="1.5" fill="none" stroke="#fff" stroke-width="1.2"/></svg>
      <span>COMPLIMENTARY HOTEL CARDS</span>
    </div>
    <div class="perk">
      <svg viewBox="0 0 34 34" aria-hidden="true"><circle cx="17" cy="17" r="15.5" fill="none" stroke="#fff" stroke-width="1.2"/><rect x="12" y="9" width="10" height="16" rx="1.5" fill="none" stroke="#fff" stroke-width="1.2"/></svg>
      <span>COMPLIMENTARY SMART DEVICES</span>
    </div>
    <div class="perk">
      <svg viewBox="0 0 34 34" aria-hidden="true"><circle cx="17" cy="17" r="15.5" fill="none" stroke="#fff" stroke-width="1.2"/><rect x="9" y="11" width="16" height="12" fill="none" stroke="#fff" stroke-width="1.2"/><line x1="9" y1="15" x2="25" y2="15" stroke="#fff" stroke-width="1.2"/></svg>
      <span>COMPLIMENTARY DINING CARDS</span>
    </div>
    <div class="perk">
      <svg viewBox="0 0 34 34" aria-hidden="true"><circle cx="17" cy="17" r="15.5" fill="none" stroke="#fff" stroke-width="1.2"/><circle cx="17" cy="17" r="8" fill="none" stroke="#fff" stroke-width="1.2"/><line x1="9" y1="17" x2="25" y2="17" stroke="#fff" stroke-width="1.2"/></svg>
      <span>COMPLIMENTARY ROUNDTRIP AIRFARE</span>
    </div>
    <div class="perk">
      <svg viewBox="0 0 34 34" aria-hidden="true"><circle cx="17" cy="17" r="15.5" fill="none" stroke="#fff" stroke-width="1.2"/><path d="M8 19 L26 19 L23 23 L11 23 Z M12 19 L12 14 L21 14 L21 19" fill="none" stroke="#fff" stroke-width="1.2"/></svg>
      <span>COMPLIMENTARY CRUISE GETAWAYS</span>
    </div>
    <div class="perk">
      <svg viewBox="0 0 34 34" aria-hidden="true"><circle cx="17" cy="17" r="15.5" fill="none" stroke="#fff" stroke-width="1.2"/><rect x="10" y="14" width="14" height="10" fill="none" stroke="#fff" stroke-width="1.2"/><line x1="17" y1="14" x2="17" y2="24" stroke="#fff" stroke-width="1.2"/><line x1="9" y1="14" x2="25" y2="14" stroke="#fff" stroke-width="1.2"/></svg>
      <span>COMPLIMENTARY ALL-INCLUSIVE VACATIONS</span>
    </div>
  </div>

  <span class="cta">START A RISK FREE TRIAL</span>
</section>

<section class="carousel" aria-label="Carousel ad cards">
  <article class="card card-intro">
    <svg width="224" height="224" style="position:absolute;inset:0" aria-hidden="true">
      <polygon points="0,0 224,0 224,8 0,64" fill="#ffffff"/>
    </svg>
    <div class="brand"><span class="dot"></span>BRIGHTLANE PROMOWORKS</div>
    <p class="headline h-top">TRIPLE YOUR SALES</p>
    <p class="headline h-big"><span class="go">OFFERING</span> <span class="free">FREE</span></p>
    <p class="headline sub">SMART DEVICES AS A <span class="bonus">BONUS</span> FOR<br>BUYING YOUR PRODUCT OR SERVICE</p>
    <span class="cta">START A RISK FREE TRIAL</span>
  </article>

  <article class="card card-watch">
    <p class="title">GIVING AWAY FREE</p>
    <div class="photo" style="left:52px;top:46px;width:120px;height:126px;border-radius:50%;background:radial-gradient(circle at 45% 42%,#4a4f5c 0%,#1b1d22 60%,rgba(27,29,34,0) 72%)" role="img" aria-label="Photo of a black smartwatch showing the time"></div>
    <div class="contact"><small>MORE INFO</small><strong>+1 555-014-2290</strong></div>
    <svg class="call" viewBox="0 0 16 20" aria-hidden="true"><rect x="0.5" y="0.5" width="15" height="19" rx="2" fill="#1b1b1b"/><path d="M5 6 Q5 13 11 14 L12 12 L10 11 L9 12 Q7 11 7 8 L8 7 L7 5 Z" fill="#ffffff"/></svg>
  </article>

  <article class="card card-buds">
    <p class="title">SMART DEVICES</p>
    <div class="photo" style="left:62px;top:46px;width:100px;height:128px;border-radius:18px;background:linear-gradient(180deg,#ffffff 0%,#e6e7ea 100%)" role="img" aria-label="Photo of white wireless earbuds above their open charging case"></div>
    <span class="cta" style="top:184px">START A RISK FREE TRIAL</span>
    <p class="url">www.brightlanepromoworks.biz</p>
  </article>

  <article class="card card-phones">
    <p class="title">TO YOUR CUSTOMER</p>
    <div class="photo" style="left:58px;top:44px;width:110px;height:118px;border-radius:50%;background:radial-gradient(circle at 50% 55%,#8a5a2a 0%,#1a1a1a 50%,rgba(26,26,26,0) 72%)" role="img" aria-label="Photo of black and gold over-ear headphones"></div>
    <span class="cta" style="top:182px">START A RISK FREE TRIAL</span>
    <p class="url">www.brightlanepromoworks.biz</p>
  </article>

  <article class="card card-bundle">
    <div class="photo" style="left:32px;top:12px;width:160px;height:160px;border-radius:50%;background:radial-gradient(circle at 50% 50%,#c978d2 0%,#b55ec0 55%,rgba(176,74,184,0) 72%)" role="img" aria-label="Photo of a device bundle: earbuds, charging case and smartwatch on a decorative circle"></div>
    <span class="cta" style="top:185px">START A RISK FREE TRIAL</span>
    <p class="url">www.brightlanepromoworks.biz</p>
  </article>
</section>

</body>
</html>
```